Website design for an edge protection barrier system

- The design must be based around the attached HPID (home page information design) called CODE HPID. I've attached Word and PDF versions - these are the same. The table boxes are just for approximate placement of information – you DON'T have to make it look exactly like this. All fonts used in the HPID are only examples - you can use any Google font you wish.

- Information only is in orange text. Copy to go on the design in black text. Some instructions are in the HPID. Please be creative!

- The design needs to be modern. Colours are to be black and white with orange ...like the logo colours.

- I've provided the images for the galleries - they are labelled and will match the name in the HPID.

- Examples of some websites that have great design... don't copy them please but they are similar in look to what we are after....
http://lanternvale.co.nz/
http://www.tukobel.co.nz/
http://www.pelhamwright.co.nz/

Width of content will be 1100 pixels when implemented as a web page. Header height (without nav bar) 150-160 pixels.

If your design is chosen the winning PSD file will have to be provided as follows…
1. Canvas size of 2000px x 2000px - 72ppi in Adobe Photoshop (CS5 compatible)
2. Width of content section is 1100px wide - centered in the canvas
3. Any button rollovers/hovers in the PSD as hidden layers.
4. All fonts used must be Google fonts (except for the fonts in the header at the top of the page).
5. You will need to supply the chosen home page plus one example page (example page as a style guide for how all other pages will look). Example page is only the header and navigational bar at the top, an empty sector in the middle with a column (180 px wide) which can be left or right aligned which means the main sector is 920 pixels wide, and then the footer at the bottom of the page

Hi all, As per the HPID for the main image gallery you must use: File 7: edge protection systems for new houses hp wednesday, 17 december 2014 04:35:4112 AND File 9: Ridgeline Bracket for new home edge protection hp wednesday, 17 december 2014 04:35:4111 Use these images so they fit next to each other with the words: Edge protection systems for new houses with timber or aluminium rails (These words must be used either on or above or below the gallery) What we are looking for is a clean modern layout of the home page. The images supplied must be used please. Thank you.

Our office is closed over the New Year holiday season so decisions on designs may be delayed.

```html
<!DOCTYPE html>
<html lang="en">
<head>
<meta charset="utf-8">
<title>Ridgeway Barriers NZ Ltd – Home</title>
<link href="https://fonts.googleapis.com/css2?family=Source+Sans+3:ital,wght@0,400;0,600;0,700;1,400;1,600;1,700&family=Kalam:wght@700&display=swap" rel="stylesheet">
<style>
:root{
  --ink:#15110d;
  --panel:#110e0b;
  --orange:#fbaa27;
  --orange-deep:#f39a12;
  --white:#ffffff;
  --text:#222;
}
*{box-sizing:border-box;margin:0;padding:0}
html,body{width:1200px;height:2195px;overflow:hidden;background:var(--white);font-family:"Source Sans 3",sans-serif;color:var(--text)}
.wrap{width:950px;margin:0 auto;position:relative}
.site-header{background:var(--ink);height:129px;border-top:2px solid #333}
.site-header .wrap{height:129px}
.brand{position:absolute;left:0;top:30px;display:flex;align-items:center;gap:12px;color:var(--orange);font-size:34px;font-weight:600;line-height:1}
.brand-dot{width:26px;height:26px;border-radius:50%;background:var(--orange)}
.brand small{display:block;font-size:13px;margin-top:4px}
.tagline{position:absolute;right:0;top:27px;color:var(--orange);font-style:italic;font-size:17.5px}
.header-phone{position:absolute;right:0;top:76px;color:var(--orange);font-size:16px}
.main-nav{height:41px;border-bottom:3px solid var(--orange);background:var(--white)}
.main-nav ul{list-style:none;display:flex;height:38px;align-items:stretch}
.main-nav li{font-size:15px;padding:0 15px;display:flex;align-items:center;color:#111}
.main-nav li.active{background:var(--orange)}
.hero{background:linear-gradient(#ececec,#d9d9d9);height:409px;padding-top:18px}
.slide{height:358px;position:relative;box-shadow:0 22px 28px -14px rgba(0,0,0,.45)}
.slide-photo{position:absolute;inset:0;background:linear-gradient(#8c9aa8 0%,#b6bcc2 38%,#a07a55 55%,#d8d4cc 78%,#7a7368 100%)}
.slide-title{position:absolute;left:60px;top:145px;color:var(--white);font-weight:600;font-size:35px;line-height:35px;text-shadow:1px 2px 3px rgba(0,0,0,.7)}
.slide-arrow{position:absolute;top:158px;width:38px;height:38px;background:var(--ink);display:flex;align-items:center;justify-content:center}
.slide-arrow.prev{left:0}.slide-arrow.next{right:0}
.dots{position:absolute;bottom:12px;left:50%;transform:translateX(-50%);display:flex;gap:10px}
.dots span{width:15px;height:15px;border-radius:50%;background:var(--orange)}
.dots span.on{background:var(--ink)}
.cards{display:grid;grid-template-columns:repeat(3,300px);gap:28px 25px;margin-top:28px}
.card{height:219px;background:var(--panel);border:1px solid var(--orange-deep);border-radius:3px;overflow:hidden;text-align:center}
.card-media{height:137px}
.card-media.soffit{background:linear-gradient(135deg,#3a5a34,#e3a91e 55%,#d6d6d0)}
.card-media.truss{background:linear-gradient(135deg,#6b3a22,#c9892c 60%,#cfd6de)}
.card-media.reroof{background:linear-gradient(#5f8fc8,#9cb8d6 45%,#e8e8e6 70%,#6d7b5c)}
.card-media.garage{background:linear-gradient(135deg,#9a8a4a,#f2b51e 50%,#b8c8d6)}
.card-media.soon{background:var(--orange);display:flex;align-items:center;justify-content:center;font-family:"Kalam",cursive;font-size:40px;line-height:48px;color:#111}
.card h3{color:var(--orange);font-style:italic;font-weight:400;font-size:19px;margin-top:8px}
.btn{display:inline-block;background:var(--orange);color:#111;font-weight:700;font-style:italic;border-radius:3px;font-size:15px;padding:3px 8px;border:1px solid #fff6}
.card .btn{margin-top:8px}
.intro-bar{margin-top:26px;height:94px;background:var(--panel);border:1px solid var(--orange-deep);border-radius:3px;display:flex;align-items:center;justify-content:space-between;padding:0 22px 0 16px}
.intro-bar p{color:var(--orange);font-size:13px;line-height:17px;width:775px}
.intro-bar .btn{font-size:16px;padding:7px 13px}
.video-panel{margin-top:28px;height:346px;background:var(--panel);border:1px solid var(--orange-deep);border-radius:3px;position:relative}
.video-frame{position:absolute;left:22px;top:26px;width:496px;height:276px;border:4px solid var(--orange);background:linear-gradient(135deg,#fafafa,#ececec)}
.video-caption{position:absolute;left:22px;width:496px;top:316px;text-align:center;color:var(--orange);font-weight:600;font-size:14px}
.video-copy{position:absolute;left:569px;right:16px;top:20px;color:var(--orange)}
.video-copy h2{font-weight:600;font-size:23px;margin-bottom:14px}
.video-copy p{font-size:13.5px;line-height:16px;text-align:justify;margin-bottom:15px}
.video-copy .btn{margin-left:112px;font-style:normal;font-weight:600;font-size:16px;padding:7px 18px}
.testimonial{margin-top:28px;height:283px;background:var(--panel);border:1px solid var(--orange-deep);border-radius:3px;position:relative}
.testimonial-photo{position:absolute;left:22px;top:23px;width:276px;height:219px;border:4px solid var(--orange);background:linear-gradient(#9a6c3c,#c8a070 40%,#5b4a3a 80%,#3a3a2f)}
.testimonial-copy{position:absolute;left:317px;right:18px;top:15px;color:var(--orange)}
.testimonial-copy h2{font-weight:600;font-size:17.5px;letter-spacing:-.2px;white-space:nowrap;margin-bottom:10px}
.testimonial-copy p{font-size:12.5px;line-height:16px;margin-bottom:15px}
.testimonial-copy .who{text-align:right;font-size:14px;margin:0;line-height:20px}
.testimonial-copy .who b{font-style:italic}
.site-footer{margin-top:26px;height:293px;background:var(--ink);border-top:3px solid var(--orange)}
.site-footer .wrap{height:100%}
.foot-col{position:absolute;top:30px;color:var(--orange)}
.foot-col ul{list-style:none}
.foot-col li{font-size:15px;line-height:25.6px}
.foot-col li::before{content:"»";margin-right:10px}
.foot-col h4{font-size:20px;font-weight:600;margin-bottom:12px}
.col-nav{left:0;top:28px}
.col-systems{left:277px}
.col-info{left:569px;right:0}
.col-info p{font-size:12.5px;line-height:15px;text-align:justify}
.col-info h5{font-size:14px;font-weight:700;margin:10px 0 8px}
.foot-phone{position:absolute;left:0;top:227px;color:var(--orange);font-weight:600;font-size:17px}
.badges{display:flex;gap:14px}
.badge{width:90px;height:90px;background:var(--white);border-radius:4px}
.social{width:278px;height:90px;background:#3b5a9a;color:var(--white);display:flex;align-items:center;gap:14px;padding-left:22px;font-size:24px;font-weight:600}
.social i{width:40px;height:40px;background:var(--white);display:block}
</style>
</head>
<body>
<header class="site-header">
  <div class="wrap">
    <div class="brand"><span class="brand-dot"></span><span>Ridgeway Barriers<small>NZ Ltd</small></span></div>
    <div class="tagline">Innovative edge protection system for the building industry - NZ wide</div>
    <div class="header-phone">0800 RDGWAY | 0800 555 014</div>
  </div>
</header>
<nav class="main-nav">
  <div class="wrap">
    <ul>
      <li class="active">Home</li><li>About Us</li><li>Edge</li><li>Protection</li><li>Systems</li><li>Safety</li><li>Testimonials</li><li>Gallery</li><li>Downloads/Videos</li><li>Quote / Contact</li>
    </ul>
  </div>
</nav>
<section class="hero">
  <div class="wrap slide">
    <div class="slide-photo" role="img" aria-label="New house frame with edge protection rails fitted along the roof trusses"></div>
    <h1 class="slide-title">EDGE PROTECTION SYSTEMS<br>For New Houses With Timber Or Aluminium Rails</h1>
    <div class="slide-arrow prev"><svg width="12" height="16" viewBox="0 0 12 16"><path d="M9 2 3 8l6 6" fill="none" stroke="#fff" stroke-width="2.5"/></svg></div>
    <div class="slide-arrow next"><svg width="12" height="16" viewBox="0 0 12 16"><path d="m3 2 6 6-6 6" fill="none" stroke="#fff" stroke-width="2.5"/></svg></div>
    <div class="dots"><span class="on"></span><span></span><span></span></div>
  </div>
</section>
<main class="wrap">
  <div class="cards">
    <article class="card"><div class="card-media soffit" role="img" aria-label="Yellow soffit mount bracket on a new build"></div><h3>New Build Soffit Mount...</h3><span class="btn">Read More</span></article>
    <article class="card"><div class="card-media truss" role="img" aria-label="Yellow truss mount bracket on timber truss"></div><h3>New Build Truss Mount...</h3><span class="btn">Read More</span></article>
    <article class="card"><div class="card-media reroof" role="img" aria-label="Re-roof house with edge rails along the roof line"></div><h3>Re-roof...</h3><span class="btn">Read More</span></article>
    <article class="card"><div class="card-media garage" role="img" aria-label="Bracket fitted to a garage gutter"></div><h3>Garage and Sheds...</h3><span class="btn">Read More</span></article>
    <article class="card"><div class="card-media soon">Coming Soon...</div><h3>Commercial...</h3><span class="btn">Read More</span></article>
    <article class="card"><div class="card-media soon">Watch This<br>Space...</div><h3>New Product...</h3><span class="btn">Read More</span></article>
  </div>
  <section class="intro-bar">
    <p>Lorem Ipsum is simply dummy text of the printing and typesetting industry. Lorem Ipsum has been the industry's standard dummy text ever since the 1500s, when an unknown printer took a galley of type and scrambled it to make a type specimen book. It has survived not only five centuries.</p>
    <span class="btn">Read More</span>
  </section>
  <section class="video-panel">
    <div class="video-frame" role="img" aria-label="Video still of the yellow roof-edge bracket">
      <svg width="488" height="268" viewBox="0 0 488 268"><circle cx="244" cy="134" r="80" fill="#ddd"/><path d="M222 94v80l64-40z" fill="#000"/></svg>
    </div>
    <div class="video-caption">Watch the video on how the Edge Protection system works...</div>
    <div class="video-copy">
      <h2>Edge Protection Systems...</h2>
      <p>Edge Protection is essential when working on buildings at height. Our systems are designed by experienced tradesmen and are manufactured in New Zealand.</p>
      <p>The Ridgeline bracket is without a doubt the most versatile and cost effective Edge Protection on the market. The Ridgeline Bracket system has been designed (and has passed stringent testing) to comply with AS/NZS 39931:2009.</p>
      <span class="btn">Find Out More</span>
    </div>
  </section>
  <section class="testimonial">
    <div class="testimonial-photo" role="img" aria-label="Building crew standing in front of a house frame"></div>
    <div class="testimonial-copy">
      <h2>"I would recommend Ridgeway Barriers NZ Ltd. to any prospective purchaser"</h2>
      <p>"Corvan Homes Ltd. has used the services of Owen Tarrant and his Ridgeway Barriers. I was impressed both with the quality of the edge protection Owen supplied and his knowledge and understanding of the new requirements being enforced by the Labour Dept.</p>
      <p>I had a meeting with the Labour Dept. representative in my office which Owen attended and Owen introduced a simple and easy way to address the issue which was more than the Labour Dept. were prepared to offer.</p>
      <p>I would recommend Ridgeway Barriers N.Z. Ltd. to any prospective purchaser."</p>
      <p class="who"><b>- Mara Lindqvist.</b><br>Director of Corvan Homes Ltd</p>
    </div>
  </section>
</main>
<footer class="site-footer">
  <div class="wrap">
    <div class="foot-col col-nav"><ul><li>Home</li><li>About Us</li><li>Safety</li><li>Testimonials</li><li>Gallery</li><li>Downloads/Videos</li><li>Quote / Contact</li></ul></div>
    <div class="foot-phone">0800 RDGWAY | 0800 555 014</div>
    <div class="foot-col col-systems"><h4>Edge Protection Systems</h4><ul><li>New Build Soffit Mount</li><li>New Build Truss Mount</li><li>Re-roof</li><li>Garage and Sheds</li><li>Commercial - Coming Soon</li><li>New product - Coming Soon</li></ul></div>
    <div class="foot-col col-info">
      <h4>Edge Protection Systems</h4>
      <p><b>Important:</b> All our systems are the property of Ridgeway Barriers NZ Ltd. It is company policy to vigorously prosecute any attempts to copy our innovations and designs.</p>
      <h5>Proudly New Zealand Made</h5>
      <div class="badges"><div class="badge"></div><div class="social"><i></i>Friendspace</div></div>
    </div>
  </div>
</footer>
</body>
</html>
```